integrative health clinic-Medical massage, acupuncture, chiropractic

we like our logo, but are open to new ideas. We need a new card design. We have added chiropractic and acupuncture that we have put under the name of the business. We are an integrative medical clinic

Target Market(s)

General public, athletes

Contact Information for Business Card

Phone 5055583927
Fax 5055583926
Hours Monday-Friday 9-6
Saturday 10-6
The 20% can be smaller on the back

Colors
3176b5
0355a3

Requirements
Must have
• Logo but am open to ideas
Nice to have
• We are an integrated medical clinic but also want to be personable. We want the card fun and inviting

```html
<!DOCTYPE html>
<html lang="en">
<head>
<meta charset="UTF-8">
<title>Evenkeel Health – Business Card</title>
<link href="https://fonts.googleapis.com/css2?family=Lato:wght@400;700;900&display=swap" rel="stylesheet">
<style>
  :root {
    --page-bg: #dcdde1;
    --card-blue-dark: #1f2f7e;
    --card-blue-mid: #24398f;
    --card-blue-light: #3552a3;
    --card-white: #ffffff;
    --ink: #111318;
    --ink-soft: #3a3d45;
    --accent: #2b3b94;
    --offer-text: #f3f3f5;
  }
  * { margin: 0; padding: 0; box-sizing: border-box; }
  html, body {
    width: 1200px;
    height: 800px;
    overflow: hidden;
    background: var(--page-bg);
    font-family: 'Lato', sans-serif;
  }
  .canvas {
    position: relative;
    width: 1200px;
    height: 800px;
  }
  .card {
    position: absolute;
    left: 358px;
    width: 484px;
    height: 276px;
    box-shadow: 0 6px 14px rgba(40, 42, 55, 0.28);
  }
  .card--offer {
    top: 100px;
    background: radial-gradient(ellipse at 85% 10%, var(--card-blue-light) 0%, var(--card-blue-mid) 55%, var(--card-blue-dark) 100%);
    color: var(--offer-text);
    display: flex;
    flex-direction: column;
    align-items: center;
    justify-content: center;
  }
  .offer__amount {
    font-weight: 900;
    font-size: 86px;
    line-height: 1;
    letter-spacing: -1px;
    margin-top: -6px;
  }
  .offer__label {
    font-weight: 700;
    font-size: 27px;
    line-height: 1;
    margin-top: 6px;
    letter-spacing: -0.3px;
  }
  .card--details {
    top: 428px;
    background: var(--card-white);
    display: flex;
    align-items: center;
    padding-left: 32px;
  }
  .brand {
    display: flex;
    align-items: center;
    gap: 10px;
    width: 214px;
  }
  .brand__dot {
    flex: none;
    width: 22px;
    height: 22px;
    border-radius: 50%;
    background: var(--accent);
  }
  .brand__name {
    font-weight: 700;
    font-size: 22px;
    color: var(--ink);
    line-height: 1.05;
  }
  .brand__tagline {
    font-weight: 700;
    font-size: 22px;
    color: var(--ink);
    line-height: 1.05;
  }
  .divider {
    width: 1px;
    height: 84px;
    background: var(--accent);
    margin: 0 10px 0 10px;
  }
  .contact {
    color: var(--ink-soft);
    font-size: 12px;
    line-height: 1.35;
  }
  .contact__hours { margin-bottom: 12px; }
  .contact__row {
    display: flex;
    align-items: center;
    gap: 5px;
  }
  .contact__icon { width: 9px; height: 9px; fill: var(--accent); flex: none; }
</style>
</head>
<body>
<main class="canvas">
  <section class="card card--offer" aria-label="Offer side">
    <div class="offer__amount">20 %</div>
    <div class="offer__label">OFF FIRST VISIT</div>
  </section>

  <section class="card card--details" aria-label="Contact side">
    <div class="brand">
      <span class="brand__dot"></span>
      <div>
        <div class="brand__name">Evenkeel Health</div>
      </div>
    </div>
    <div class="divider"></div>
    <div class="contact">
      <div class="contact__hours">
        <div>Monday-Friday 9-6</div>
        <div>Saturday 10-6</div>
      </div>
      <div class="contact__row">
        <svg class="contact__icon" viewBox="0 0 10 10" aria-hidden="true"><path d="M2 0.5 L3.6 0.5 L4.2 2.8 L3 3.6 C3.6 5 4.9 6.4 6.4 7 L7.2 5.8 L9.5 6.4 L9.5 8 C9.5 9 8.6 9.6 7.6 9.4 C4.2 8.6 1.4 5.8 0.6 2.4 C0.4 1.4 1 0.5 2 0.5 Z"/></svg>
        <span>5055583927</span>
      </div>
      <div class="contact__row">
        <svg class="contact__icon" viewBox="0 0 10 10" aria-hidden="true"><rect x="2.5" y="0.5" width="5" height="2.5"/><rect x="0.5" y="3.5" width="9" height="4" rx="0.8"/><rect x="2.5" y="6.5" width="5" height="3"/></svg>
        <span>5055583926</span>
      </div>
      <div class="contact__row">
        <svg class="contact__icon" viewBox="0 0 10 10" aria-hidden="true"><path d="M5 0.5 A4.5 4.5 0 1 0 5 9.5 A4.5 4.5 0 1 0 5 0.5 Z M5 1.4 C5.8 2.2 6.2 3.4 6.3 4.5 L3.7 4.5 C3.8 3.4 4.2 2.2 5 1.4 Z M1.5 5.5 L2.8 5.5 C2.9 6.6 3.2 7.6 3.8 8.4 C2.6 8 1.7 6.9 1.5 5.5 Z M3.7 5.5 L6.3 5.5 C6.2 6.6 5.8 7.8 5 8.6 C4.2 7.8 3.8 6.6 3.7 5.5 Z M1.5 4.5 C1.7 3.1 2.6 2 3.8 1.6 C3.2 2.4 2.9 3.4 2.8 4.5 Z M6.2 1.6 C7.4 2 8.3 3.1 8.5 4.5 L7.2 4.5 C7.1 3.4 6.8 2.4 6.2 1.6 Z M7.2 5.5 L8.5 5.5 C8.3 6.9 7.4 8 6.2 8.4 C6.8 7.6 7.1 6.6 7.2 5.5 Z"/></svg>
        <span>www.evenkeelhealth.com</span>
      </div>
    </div>
  </section>
</main>
</body>
</html>
```